Homepage for the brisk-trail Web Application

At the end of this text, you will find a link to a website that is under construction for a webApp that I intend to launch soon. The contest goal is for you to make redesign the homepage in a nice, fresh, modern Style. Only design, no coding necessary. It needs to have a responsive version for small screens like smart phones. Attached is the text for it, and some images that you may use. You are welcome to find or create additional supporting images. You can use PixVaultimages.com or similar service to find new images as long as I can purchase the non-exclusive use rights for the images at similar prices. The contest is just for the home page. However, the winner, if I like the work and we can agree on a fair price, could be contracted on a one-on-one basis to do the rest of the site. You are welcome to suggest minor changes like font sizes and minor variations on the Header banner, but that banner is consistent with the user interface of the application therefore should not change too much. The information should flow somewhat continually without much use of side bars or things like that.
https://www.brisk-trail-example.com
Sincerely,
Marco R. Delgado

```html
<!DOCTYPE html>
<html lang="en">
<head>
<meta charset="utf-8">
<title>Brisk-Trail — Find any document or item instantly</title>
<link href="https://fonts.googleapis.com/css2?family=Poppins:wght@400;500;600&display=swap" rel="stylesheet">
<style>
  :root {
    --orange: #ff7b52;
    --ink: #111111;
    --text: #2a2a2a;
    --cyan-soft: #dcfbfd;
    --cyan-ring: #c4f1f5;
    --white: #ffffff;
    --footer: #000000;
  }
  * { box-sizing: border-box; margin: 0; padding: 0; }
  html, body { width: 1200px; height: 3571px; overflow: hidden; background: var(--white); }
  body { font-family: "Poppins", sans-serif; color: var(--text); }
  .page { position: relative; width: 1200px; height: 3571px; overflow: hidden; }
  .abs { position: absolute; }
  .accent { color: var(--orange); }

  /* header */
  .brand { left: 97px; top: 18px; display: flex; align-items: center; gap: 8px; font-size: 20px; color: var(--orange); font-weight: 400; }
  .brand-dot { width: 26px; height: 26px; border-radius: 50%; border: 2px solid #333; }
  .nav { left: 306px; top: 26px; display: flex; gap: 32px; font-size: 14px; color: var(--ink); }
  .btn { display: inline-flex; align-items: center; justify-content: center; border-radius: 20px; font-size: 12px; font-family: "Poppins", sans-serif; }
  .btn-solid { background: var(--orange); color: var(--white); box-shadow: 0 4px 10px rgba(255,123,82,.35); }
  .btn-ghost { border: 1.5px solid var(--orange); color: var(--orange); background: var(--white); }
  .login { left: 1019px; top: 21px; width: 99px; height: 29px; }

  /* hero */
  .hero-title { left: 97px; top: 172px; font-size: 49px; font-weight: 600; line-height: 68px; color: var(--ink); }
  .hero-copy { left: 97px; top: 328px; width: 450px; font-size: 15px; line-height: 26px; }
  .hero-pricing { left: 97px; top: 459px; width: 115px; height: 33px; }
  .hero-trial { left: 238px; top: 459px; width: 114px; height: 33px; }

  .illus { border-radius: 50%; background: radial-gradient(circle, #e9fdfe 0%, var(--cyan-soft) 62%, var(--cyan-ring) 100%); box-shadow: 0 6px 18px rgba(0,0,0,.06); }
  .illus::after { content: ""; position: absolute; inset: 40px; border-radius: 50%; border: 2px solid rgba(255,255,255,.8); background: linear-gradient(160deg, rgba(76,196,208,.35), rgba(255,123,82,.18)); }

  .section-title { left: 0; width: 1200px; text-align: center; font-size: 35px; font-weight: 600; line-height: 52px; color: var(--ink); }

  .block-heading { font-size: 27px; font-weight: 500; color: var(--ink); }
  .block-copy { font-size: 13.5px; line-height: 24.2px; }

  /* accordion */
  .accordion { left: 137px; top: 1397px; width: 458px; list-style: none; }
  .accordion li { height: 44px; margin-bottom: 12.7px; border-radius: 22px; background: var(--white); box-shadow: 0 2px 8px rgba(0,0,0,.12); display: flex; align-items: center; justify-content: space-between; padding: 0 18px 0 26px; font-size: 13.5px; color: var(--ink); }
  .accordion .plus { color: var(--orange); font-size: 20px; font-weight: 400; }

  /* why list */
  .why-list { list-style: none; font-size: 17px; line-height: 24px; color: var(--ink); }
  .why-list li { position: relative; padding-left: 42px; margin-bottom: 12px; }
  .why-list svg { position: absolute; left: 0; top: 2px; }

  .cta { left: 502px; top: 2735px; width: 195px; height: 39px; font-size: 16px; }

  .footer { left: 0; top: 2816px; width: 1200px; height: 47px; background: var(--footer); color: var(--white); font-size: 13.5px; display: flex; align-items: center; justify-content: center; }
</style>
</head>
<body>
<div class="page">

  <header>
    <div class="abs brand"><span class="brand-dot"></span>Brisk Trail</div>
    <nav class="abs nav">
      <span>About</span><span>Pricing</span><span>Blog</span><span>FAQs</span><span>Support</span><span>Reviews</span><span>Contact Us</span><span>Free-Trial</span>
    </nav>
    <a class="abs btn btn-solid login">login</a>
  </header>

  <section class="hero">
    <h1 class="abs hero-title">Find any document or<br>item <span class="accent">instantly!</span></h1>
    <p class="abs hero-copy">Brisk-Trail is a system that allows you to quickly search for the location of every item that you store or file. It is an essential tool for keeping track of paper documents or any other kind of physical item.</p>
    <a class="abs btn btn-solid hero-pricing">Get Pricing</a>
    <a class="abs btn btn-ghost hero-trial">Free Trial</a>
    <div class="abs illus" style="left:676px;top:121px;width:438px;height:438px;" role="img" aria-label="Illustration of a businessman filing folders into drawers inside a laptop"></div>
  </section>

  <h2 class="abs section-title" style="top:618px;">Why use a storage management system<br>like <span class="accent">Brisk-Trail?</span></h2>

  <section class="paper">
    <div class="abs illus" style="left:65px;top:758px;width:436px;height:436px;" role="img" aria-label="Illustration of a man carrying a large binder out of a smartphone filing cabinet"></div>
    <h3 class="abs block-heading" style="left:577px;top:790px;">Managing paper documents</h3>
    <p class="abs block-copy" style="left:577px;top:840px;width:530px;">It is quite common for most people and businesses to receive a variety of such documents that need to be filed. The problem is how to efficiently do it in a way that any of it can easily be found, even in a distant future. We normally put them in folders on file drawers sorted by some criteria. But which criterion is the right standard for all kinds of documents? There is no right criterion for every kind of document. It is necessary to use a combination of them. If after some time you do not remember which criterion you used to file a document, you may have a hard time finding it, or not find it at all. This problem is greatly intensified when the person looking for the document is not the same person that filed it. It is estimated that workers spend over 20% of their time managing documents. A storage management system like Brisk-Trail would allow any authorized user to instantly find any document regardless of who filed it or which criterion was used, as long as it was properly filed using the system.</p>
  </section>

  <section class="objects">
    <h3 class="abs block-heading" style="left:137px;top:1270px;">Managing any non-document objects</h3>
    <p class="abs block-copy" style="left:137px;top:1323px;width:440px;">The same is true of storing any other kind of objects. Common examples include</p>
    <ul class="abs accordion">
      <li>Storage boxes, closets, warehouses, and shelves<span class="plus">+</span></li>
      <li>Books<span class="plus">+</span></li>
      <li>Wines<span class="plus">+</span></li>
      <li>Safety boxes<span class="plus">+</span></li>
      <li>Moving boxes<span class="plus">+</span></li>
      <li>Test samples<span class="plus">+</span></li>
      <li>Audio, video, data, and removable media<span class="plus">+</span></li>
      <li>Keys<span class="plus">+</span></li>
    </ul>
    <div class="abs illus" style="left:735px;top:1337px;width:436px;height:436px;" role="img" aria-label="Illustration of a man holding a test tube beside a smartphone filing cabinet"></div>
  </section>

  <section class="alternative">
    <div class="abs illus" style="left:63px;top:1926px;width:436px;height:436px;" role="img" aria-label="Illustration of a man holding a wine bottle beside a smartphone filing cabinet"></div>
    <h2 class="abs" style="left:607px;top:1992px;font-size:35px;font-weight:600;line-height:50px;color:var(--ink);">Alternative uses for<br><span class="accent">Brisk-Trail</span></h2>
    <p class="abs block-copy" style="left:607px;top:2125px;width:432px;">How many times have you gone to a restaurant and couldn't recall how good (or bad) each of the dishes were that you previously ordered? You can use Brisk-Trail to record each one to improve your experience for every visit. Our app can also help you decide where you want to go or which dish to recommend when you have a special occasion.</p>
    <a class="abs btn btn-solid" style="left:607px;top:2293px;width:123px;height:31px;font-size:13px;">Get Started</a>
  </section>

  <section class="why">
    <h2 class="abs section-title" style="top:2412px;">Why <span class="accent">Brisk-Trail?</span></h2>
    <ul class="abs why-list" style="left:95px;top:2523px;width:460px;">
      <li><svg width="28" height="20" viewBox="0 0 28 20"><path d="M2 10l8 7L26 2" fill="none" stroke="#ff7b52" stroke-width="4" stroke-linecap="round" stroke-linejoin="round"/></svg>It is extremely easy to use.</li>
      <li><svg width="28" height="20" viewBox="0 0 28 20"><path d="M2 10l8 7L26 2" fill="none" stroke="#ff7b52" stroke-width="4" stroke-linecap="round" stroke-linejoin="round"/></svg>It's very affordable. Checkout our pricing plans!</li>
      <li><svg width="28" height="20" viewBox="0 0 28 20"><path d="M2 10l8 7L26 2" fill="none" stroke="#ff7b52" stroke-width="4" stroke-linecap="round" stroke-linejoin="round"/></svg>Since it is online, your data is available almost anywhere in the world.</li>
    </ul>
    <ul class="abs why-list" style="left:638px;top:2523px;width:475px;">
      <li><svg width="28" height="20" viewBox="0 0 28 20"><path d="M2 10l8 7L26 2" fill="none" stroke="#ff7b52" stroke-width="4" stroke-linecap="round" stroke-linejoin="round"/></svg>It Adapts to your stile. Since each catalog can have 1 or more levels of depth (folders and sub-folders), Brisk-Trail does not force you to use a specific filing or storage methodology.</li>
      <li><svg width="28" height="20" viewBox="0 0 28 20"><path d="M2 10l8 7L26 2" fill="none" stroke="#ff7b52" stroke-width="4" stroke-linecap="round" stroke-linejoin="round"/></svg>Data encryption ensures that your information is always private, safe, and secure.</li>
    </ul>
    <a class="abs btn btn-solid cta">30 Days Free Trial</a>
  </section>

  <footer class="abs footer">© Copyright 2021 brisk-trail .All Rights Reserved.</footer>
</div>
</body>
</html>
```